Reliable and clean label for a natural product!

We would like to have a label design for our CBD SOFT GEL CAPSULES . We are a business family and believe in the power of natural healing. In this label we would like to show a reliable, natural and feminine product mainly.

Font styles to use
Serif
Sans Serif

Colors

Designer to choose colors to be used in the design.

```html
<!DOCTYPE html>
<html lang="en">
<head>
<meta charset="UTF-8">
<title>CBD Oil Capsules Label</title>
<link href="https://fonts.googleapis.com/css2?family=Anton&family=Arimo:wght@400;700&display=swap" rel="stylesheet">
<style>
  :root {
    --canvas-bg: #e4e4e4;
    --label-bg: #2a2627;
    --title-green: #5ec54a;
    --band-green: #6fd34f;
    --band-green-light: #a8e86a;
    --accent-yellow: #f2ec3a;
    --text-white: #f4f4f4;
    --text-dark: #1c1a1a;
    --leaf-dark: #1f4a2a;
    --leaf-mid: #2f7a3e;
  }
  * { margin: 0; padding: 0; box-sizing: border-box; }
  html, body { width: 1200px; height: 800px; overflow: hidden; }
  body {
    background: var(--canvas-bg);
    font-family: "Arimo", Arial, sans-serif;
    position: relative;
  }
  .label {
    position: absolute;
    left: 140px; top: 180px;
    width: 920px; height: 440px;
    background: var(--label-bg);
    overflow: hidden;
  }
  .leaf-art {
    position: absolute;
    border-radius: 50%;
  }
  .leaf-art--center {
    left: 300px; top: 120px; width: 360px; height: 300px;
    background: radial-gradient(ellipse at center, var(--leaf-mid) 0%, var(--leaf-dark) 45%, rgba(31,74,42,0) 72%);
  }
  .leaf-art--right {
    left: 720px; top: 60px; width: 220px; height: 260px;
    background: radial-gradient(ellipse at center, var(--leaf-mid) 0%, var(--leaf-dark) 45%, rgba(31,74,42,0) 72%);
  }
  .leaf-art--small {
    width: 80px; height: 70px;
    background: radial-gradient(ellipse at center, rgba(47,122,62,.5) 0%, rgba(31,74,42,0) 70%);
  }
  .leaf-art--tl { left: 60px; top: 10px; }
  .leaf-art--bl { left: 40px; top: 300px; }
  .leaf-art--br { left: 840px; top: 360px; }

  .side-tagline {
    position: absolute;
    left: 58px; top: 340px;
    transform: rotate(-90deg);
    transform-origin: left top;
    font-size: 19px;
    color: var(--text-white);
    white-space: nowrap;
  }
  .side-tagline .accent { color: var(--accent-yellow); }

  .product-title {
    position: absolute;
    left: 190px; top: 40px;
    font-family: "Anton", Impact, sans-serif;
    font-size: 66px;
    line-height: 0.9;
    color: var(--title-green);
    letter-spacing: 1px;
    text-transform: uppercase;
  }
  .extract-bar {
    position: absolute;
    left: 180px; top: 252px;
    width: 400px; height: 46px;
    background: var(--accent-yellow);
    color: var(--text-dark);
    font-size: 20px;
    line-height: 46px;
    padding-left: 26px;
    white-space: nowrap;
  }
  .extract-bar strong { font-weight: 700; }
  .potency {
    position: absolute;
    left: 180px; top: 318px;
    padding-left: 20px;
    border-left: 3px solid var(--accent-yellow);
    color: var(--text-white);
    font-size: 20px;
    line-height: 1.15;
  }
  .count {
    position: absolute;
    right: 52px; top: 316px;
    text-align: center;
    color: var(--accent-yellow);
  }
  .count .number {
    display: block;
    font-family: "Anton", Impact, sans-serif;
    font-size: 52px;
    line-height: 1;
  }
  .count .unit { display: block; font-size: 15px; font-weight: 700; }
  .base-band {
    position: absolute;
    left: 0; bottom: 0;
    width: 100%; height: 14px;
    background: linear-gradient(90deg, var(--band-green), var(--band-green-light));
  }
</style>
</head>
<body>
  <section class="label">
    <div class="leaf-art leaf-art--center" role="img" aria-label="Illustrated hemp leaves behind the title"></div>
    <div class="leaf-art leaf-art--right" role="img" aria-label="Illustrated hemp leaf at the right edge"></div>
    <div class="leaf-art leaf-art--small leaf-art--tl" role="img" aria-label="Small faint hemp leaf"></div>
    <div class="leaf-art leaf-art--small leaf-art--bl" role="img" aria-label="Small faint hemp leaf"></div>
    <div class="leaf-art leaf-art--small leaf-art--br" role="img" aria-label="Small faint hemp leaf"></div>

    <p class="side-tagline"><span class="accent">Restorative</span> Supplement</p>

    <h1 class="product-title">Capsulas<br>Aceite de<br>CBD</h1>

    <p class="extract-bar"><strong>HEMP OIL EXTRACT</strong> CAPSULES</p>

    <p class="potency">Full Spectrum<br>25 mg CBD per capsule</p>

    <p class="count"><span class="number">30</span><span class="unit">Capsules</span></p>

    <div class="base-band"></div>
  </section>
</body>
</html>
```